Trading journal (Corvanta Loop)

I need a design for trading journal application.
I would like to start from dark version of the design and the main goal that it should be pretty intuitive for everyone. I am going to create the app from scratch and I don't have any logo or branding colors, so it is up to you to choose a color scheme but it is a dark mode, so one of the colors would be black obviously.
The app will be available for web PC, Android and iOS.

There is google document with the requirements.
https://files.plomivex.net/sheet/7QwZrT2kLpN9vB4xHs0Jd8YcGm3FaUe6/view?mode=open

Target Market(s)

Professional traders

Industry/Entity Type

Trading

Colors

Designer to choose colors to be used in the design.

Requirements
Must have
• Dark mode design for PC and mobile views, the design must be pretty intuitive for everyone.
Nice to have
• Tooltips for something non obvious; popovers after completing some actions

```html
<!DOCTYPE html>
<html lang="en">
<head>
<meta charset="utf-8">
<title>Corvanta Loop – Trading Journal</title>
<link rel="stylesheet" href="https://fonts.googleapis.com/css2?family=Poppins:wght@400;500;600;700&family=Roboto:wght@400;500&display=swap">
<style>
  :root{
    --stage:#6c6c6c;
    --ink:#020a14;
    --black:#000000;
    --blue:#0a92d8;
    --frame:#1a9fe6;
    --white:#ffffff;
    --muted:#b9c0cb;
    --line:#26303e;
    --panel:#0b1552;
    --gray-bar:#5d5d5d;
  }
  *{box-sizing:border-box;margin:0;padding:0}
  html,body{width:711px;height:1200px;overflow:hidden}
  body{
    position:relative;
    background:radial-gradient(ellipse at 50% 45%,#8a8a8a 0%,var(--stage) 60%,#585858 100%);
    font-family:"Roboto",sans-serif;color:var(--white);
  }
  .screen{position:absolute;left:52px;width:607px;background:var(--ink);overflow:hidden}
  .screen--welcome{top:42px;height:321px}
  .screen--setup{top:375px;height:320px}
  .screen--dashboard{top:705px;height:453px;background:#03060c}

  .frame{position:absolute;left:20px;top:23px;width:567px;height:275px;border:2px solid var(--frame);overflow:hidden}
  .screen--setup .frame{top:22px;height:276px}
  .hero-art{position:absolute;inset:0}
  .hero-art--market{
    background:
      radial-gradient(ellipse 18% 22% at 8% 82%,rgba(255,110,80,.55),transparent 70%),
      radial-gradient(ellipse 22% 35% at 48% 25%,rgba(255,214,80,.55),transparent 70%),
      radial-gradient(ellipse 16% 30% at 62% 42%,rgba(255,120,40,.45),transparent 70%),
      radial-gradient(ellipse 30% 25% at 85% 80%,rgba(40,150,255,.45),transparent 70%),
      linear-gradient(160deg,#0d3d86 0%,#0a2a66 45%,#06183e 100%);
  }
  .hero-art--graph{
    background:
      radial-gradient(ellipse 12% 14% at 80% 12%,rgba(70,170,255,.6),transparent 70%),
      radial-gradient(ellipse 40% 30% at 15% 80%,rgba(30,90,180,.45),transparent 70%),
      radial-gradient(ellipse 35% 40% at 90% 60%,rgba(30,100,200,.4),transparent 70%),
      linear-gradient(180deg,#050c24 0%,#071233 60%,#0a1a44 100%);
  }
  .avatar{position:absolute;width:28px;height:28px;border-radius:50%;
    background:radial-gradient(circle at 50% 40%,#d9c4b4 0%,#8a6e5e 60%,#3b3b3b 100%);
    border:3px solid #07101c}

  .brand{font-family:"Poppins",sans-serif;font-weight:700;letter-spacing:-.2px;white-space:nowrap}
  .brand .accent{color:var(--blue)}

  .welcome-box{position:absolute;left:100px;top:159px;width:408px;height:111px;background:rgba(0,0,0,.9);border-radius:2px;text-align:center}
  .welcome-box .brand{position:absolute;left:0;right:0;top:13px;font-size:24px;line-height:30px}
  .welcome-copy{position:absolute;left:10px;right:10px;top:61px;font-size:9.6px;line-height:14px;color:var(--white)}

  .setup-panel{position:absolute;left:131px;top:67px;width:346px;height:185px;background:rgba(11,21,82,.88)}
  .setup-panel .brand{position:absolute;left:0;right:0;top:11px;text-align:center;font-size:24px;line-height:30px}
  .field{position:absolute;width:147px;height:23px;border:1px solid rgba(255,255,255,.75);
    font-size:6.4px;line-height:21px;padding-left:9px;color:var(--white)}
  .field--select::after{content:"";position:absolute;right:9px;top:9px;border:3px solid transparent;border-top:3.5px solid var(--white)}
  .submit{position:absolute;left:144px;top:132px;width:56px;height:23px;border-radius:12px;background:var(--blue);
    font-size:7.4px;font-weight:500;line-height:23px;text-align:center;letter-spacing:.2px}

  .sidebar{position:absolute;left:0;top:25px;width:39px;height:428px;background:var(--black)}
  .topbar{position:absolute;left:0;top:0;width:607px;height:25px;background:var(--black)}
  .add-btn{position:absolute;left:8px;top:9px;width:25px;height:17px;border-radius:2px;background:var(--blue);
    font-size:10px;line-height:17px;text-align:center;font-weight:400}
  .topbar .brand{position:absolute;left:47px;top:3px;font-size:15px;line-height:20px}
  .nav-icons{position:absolute;left:0;top:0}
  .bell{position:absolute;left:551px;top:6px}
  .screen--dashboard .avatar{left:569px;top:2px;width:22px;height:22px;border-width:2px}

  .main-bg{position:absolute;left:39px;top:25px;width:568px;height:428px;
    background:radial-gradient(ellipse 60% 40% at 70% 100%,rgba(20,50,110,.55),transparent 70%),#03060c}

  .card{position:absolute;background:var(--black);border:1px solid var(--line)}
  .card-label{position:absolute;left:17px;top:10px;font-family:"Poppins",sans-serif;font-weight:600;font-size:6.6px;line-height:10px;text-transform:uppercase;color:var(--white)}
  .stat{top:44px;width:132px;height:55px}
  .stat-value{position:absolute;left:17px;top:25px;font-family:"Poppins",sans-serif;font-weight:600;font-size:12.8px;color:var(--blue)}
  .stat-go{position:absolute;left:104px;top:28px}
  .chart-card{top:109px;width:176px;height:140px}
  .chart-card svg{position:absolute;left:0;top:0}
  .legend{font-family:"Poppins",sans-serif;font-weight:500;font-size:6px;fill:var(--white)}
  .axis{font-family:"Poppins",sans-serif;font-size:3.2px;fill:var(--muted)}

  .trades{left:51px;top:259px;width:546px;height:164px}
  .trades .card-label{left:17px;top:16px}
  .pager{position:absolute;right:18px;top:17px;display:flex;gap:3px}
  .pager span{width:10px;height:10px;border-radius:50%;background:#0a6fb0;position:relative}
  .trade-table{position:absolute;left:17px;top:39px;width:510px;border-collapse:collapse;font-family:"Poppins",sans-serif}
  .trade-table th{height:25px;font-size:5.4px;font-weight:600;text-transform:uppercase;background:#03070e;text-align:left;border-bottom:1px solid var(--line)}
  .trade-table td{height:25px;font-size:5.4px;border-bottom:1px solid var(--line)}
  .trade-table .logo-cell{font-size:11px;color:#8d8d8d;font-weight:400;letter-spacing:.5px}
  .trade-table tr{border-left:1px solid var(--line);border-right:1px solid var(--line)}

  .footer{position:absolute;left:39px;right:0;top:434px;text-align:center;font-family:"Poppins",sans-serif;font-size:6.6px;color:var(--white)}
</style>
</head>
<body>

<section class="screen screen--welcome">
  <div class="frame">
    <div class="hero-art hero-art--market" role="img" aria-label="Photo of glowing candlestick price chart over a dotted world map"></div>
    <div class="welcome-box">
      <h1 class="brand">Trading <span class="accent">Journal</span></h1>
      <p class="welcome-copy">Welcome to Corvanta Loop. Corvanta Loop helps you learn from your trade mistakes and<br>become a profitable trader with the power of journaling and analytics</p>
    </div>
  </div>
  <div class="avatar" role="img" aria-label="User profile photo" style="left:564px;top:16px"></div>
</section>

<section class="screen screen--setup">
  <div class="frame">
    <div class="hero-art hero-art--graph" role="img" aria-label="Photo of glowing blue market line charts on a dark background"></div>
  </div>
  <div class="setup-panel">
    <h1 class="brand">Trading <span class="accent">Journal</span></h1>
    <div class="field" style="left:22px;top:63px">Enter Display Name</div>
    <div class="field field--select" style="left:176px;top:63px">What is your default account currency?</div>
    <div class="field field--select" style="left:22px;top:95px">What is your default time zone?</div>
    <div class="field field--select" style="left:176px;top:95px">What is your trading experience?</div>
    <div class="submit">SUBMIT</div>
  </div>
  <div class="avatar" role="img" aria-label="User profile photo" style="left:564px;top:15px"></div>
</section>

<section class="screen screen--dashboard">
  <div class="main-bg"></div>
  <div class="topbar">
    <div class="add-btn">+</div>
    <h1 class="brand">Trading <span class="accent">Journal</span></h1>
    <svg class="bell" width="14" height="14" viewBox="0 0 14 14">
      <path d="M3.5 10V6.5a3.5 3.5 0 0 1 7 0V10l1 1h-9z" fill="none" stroke="#fff" stroke-width=".9"/>
      <path d="M6 12h2" stroke="#fff" stroke-width=".9"/>
      <circle cx="10.5" cy="2.5" r="2" fill="#0a92d8"/>
    </svg>
    <div class="avatar" role="img" aria-label="User profile photo"></div>
  </div>

  <aside class="sidebar">
    <svg class="nav-icons" width="39" height="428" viewBox="0 0 39 428" fill="#c9ced6">
      <g transform="translate(20 20)"><circle cx="-2" cy="-2" r="1.5"/><circle cx="2" cy="-2" r="1.5"/><circle cx="-2" cy="2" r="1.5"/><circle cx="2" cy="2" r="1.5"/></g>
      <g transform="translate(20 40)"><rect x="-3.5" y="-1" width="1.5" height="4"/><rect x="-1" y="-4" width="1.5" height="7"/><rect x="1.5" y="-2" width="1.5" height="5"/></g>
      <g transform="translate(20 59)"><rect x="-3" y="-3.5" width="6" height="7" rx="1"/></g>
      <g transform="translate(20 79)"><rect x="-3.5" y="-3.5" width="7" height="7" rx="2"/></g>
      <g transform="translate(20 99)"><circle r="3.5"/></g>
      <g transform="translate(20 118)"><path d="M-4 -1 0 -3.5 4 -1 0 1.5z M-2.5 1 0 2.5 2.5 1 2.5 3 0 4 -2.5 3z"/></g>
      <g transform="translate(20 138)"><path d="M-4 -3h3.5v7H-4z M0.5 -3H4v7H0.5z"/></g>
      <g transform="translate(20 158)"><rect x="-3.5" y="-3.5" width="7" height="3" rx=".5"/><rect x="-3.5" y=".5" width="7" height="3" rx=".5"/></g>
      <g transform="translate(20 177)"><circle r="3.5"/></g>
      <g transform="translate(20 197)"><rect x="-3.5" y="-3.5" width="7" height="7" rx="1" fill="none" stroke="#c9ced6" stroke-width="1"/><circle cy="-.5" r="1.3"/></g>
      <g transform="translate(20 217)"><path d="M-3.5 -3.5h5l2 2v5h-7z"/></g>
    </svg>
  </aside>

  <div class="card stat" style="left:51px">
    <div class="card-label">Total Net Profit</div>
    <div class="stat-value">$37.8992</div>
    <svg class="stat-go" width="14" height="14" viewBox="0 0 14 14"><circle cx="7" cy="7" r="6" fill="none" stroke="#fff" stroke-width=".9"/><path d="M4 7h6M7.5 4.5 10 7l-2.5 2.5" fill="none" stroke="#fff" stroke-width=".9"/></svg>
  </div>
  <div class="card stat" style="left:189px">
    <div class="card-label">Average Win/Loss</div>
    <div class="stat-value">$27.892</div>
    <svg class="stat-go" width="14" height="14" viewBox="0 0 14 14"><circle cx="7" cy="7" r="6" fill="none" stroke="#fff" stroke-width=".9"/><path d="M4 7h6M7.5 4.5 10 7l-2.5 2.5" fill="none" stroke="#fff" stroke-width=".9"/></svg>
  </div>
  <div class="card stat" style="left:327px">
    <div class="card-label">Total Number of Trades</div>
    <div class="stat-value">$49.800</div>
    <svg class="stat-go" width="14" height="14" viewBox="0 0 14 14"><circle cx="7" cy="7" r="6" fill="none" stroke="#fff" stroke-width=".9"/><path d="M4 7h6M7.5 4.5 10 7l-2.5 2.5" fill="none" stroke="#fff" stroke-width=".9"/></svg>
  </div>
  <div class="card stat" style="left:465px">
    <div class="card-label">Win Rate</div>
    <div class="stat-value">$67.892</div>
    <svg class="stat-go" width="14" height="14" viewBox="0 0 14 14"><circle cx="7" cy="7" r="6" fill="none" stroke="#fff" stroke-width=".9"/><path d="M4 7h6M7.5 4.5 10 7l-2.5 2.5" fill="none" stroke="#fff" stroke-width=".9"/></svg>
  </div>

  <div class="card chart-card" style="left:51px">
    <div class="card-label">Fees + Commissions</div>
    <svg width="176" height="140" viewBox="0 0 176 140">
      <circle cx="64" cy="78" r="44" fill="none" stroke="#6a6a6a" stroke-width="4"/>
      <path d="M64 34 A44 44 0 0 1 107.6 84" fill="none" stroke="#0a92d8" stroke-width="4"/>
      <text x="64" y="80" text-anchor="middle" font-family="Poppins,sans-serif" font-weight="600" font-size="21" fill="#fff">80%</text>
      <circle cx="117" cy="107" r="2" fill="#6a6a6a"/><text class="legend" x="123" y="109">Fees</text>
      <circle cx="117" cy="121" r="2" fill="#0a92d8"/><text class="legend" x="123" y="123">Commissions</text>
    </svg>
  </div>

  <div class="card chart-card" style="left:236px">
    <div class="card-label">Last Data Synced at Datetime</div>
    <svg width="176" height="140" viewBox="0 0 176 140">
      <circle cx="100" cy="38" r="2" fill="#7a7a7a"/><text class="legend" x="106" y="40">LOREM</text>
      <circle cx="100" cy="52" r="2" fill="#0a92d8"/><text class="legend" x="106" y="54">IPSUM</text>
      <g class="axis" text-anchor="end">
        <text x="11" y="58">25</text><text x="11" y="71">20</text><text x="11" y="84">15</text>
        <text x="11" y="97">10</text><text x="11" y="110">5</text><text x="11" y="124">0</text>
      </g>
      <rect x="18" y="58" width="5.5" height="65" fill="var(--gray-bar)"/>
      <rect x="30.6" y="90" width="5.5" height="33" fill="#0a92d8"/>
      <rect x="42.6" y="86" width="5.5" height="37" fill="var(--gray-bar)"/>
      <rect x="54.6" y="70" width="5.5" height="53" fill="#0a92d8"/>
      <rect x="66.5" y="90" width="5.5" height="33" fill="var(--gray-bar)"/>
      <rect x="78.5" y="90" width="5.5" height="33" fill="#0a92d8"/>
      <rect x="90.5" y="106" width="5.5" height="17" fill="var(--gray-bar)"/>
      <rect x="102.9" y="78" width="5.5" height="45" fill="#0a92d8"/>
      <g class="axis" text-anchor="middle">
        <text x="20.5" y="132">1</text><text x="33.4" y="132">2</text><text x="45.4" y="132">3</text>
        <text x="57.4" y="132">4</text><text x="69.3" y="132">5</text><text x="81.3" y="132">6</text><text x="93.3" y="132">7</text>
      </g>
      <text x="123" y="113" font-family="Poppins,sans-serif" font-size="5.2" fill="#fff">Last time Synced</text>
      <text x="123" y="123" font-family="Poppins,sans-serif" font-size="5.2" fill="#fff">Jan 16,2023</text>
    </svg>
  </div>

  <div class="card chart-card" style="left:421px">
    <div class="card-label">P&amp;L Graph with Gross /<br>Net Switcher</div>
    <svg width="176" height="140" viewBox="0 0 176 140">
      <g stroke="#1e2a3a" stroke-width=".5">
        <line x1="27" y1="37" x2="27" y2="123"/><line x1="38.6" y1="37" x2="38.6" y2="123"/><line x1="50" y1="37" x2="50" y2="123"/>
        <line x1="61" y1="37" x2="61" y2="123"/><line x1="73" y1="37" x2="73" y2="123"/><line x1="85" y1="37" x2="85" y2="123"/>
        <line x1="97" y1="37" x2="97" y2="123"/><line x1="108" y1="37" x2="108" y2="123"/><line x1="120" y1="37" x2="120" y2="123"/>
        <line x1="132" y1="37" x2="132" y2="123"/><line x1="143" y1="37" x2="143" y2="123"/><line x1="154" y1="37" x2="154" y2="123"/>
        <line x1="165" y1="37" x2="165" y2="123"/>
      </g>
      <g class="axis" text-anchor="end">
        <text x="14" y="66">120</text><text x="14" y="76">110</text><text x="14" y="85">100</text>
        <text x="14" y="95">90</text><text x="14" y="104">80</text><text x="14" y="113">70</text><text x="14" y="122">60</text>
      </g>
      <path d="M16.5 108 L38.6 80.3 L61.1 112.9 L73.1 112.9 L85 92.3 L97 112.9 L107.5 100.9 L119.5 103.3 L131.5 113.8 L142.5 113.8 L153.5 99.5 L164 115.3 L164 123.4 L16.5 123.4Z" fill="rgba(10,146,216,.35)" stroke="#0a92d8" stroke-width=".9"/>
      <line x1="16" y1="123.4" x2="168" y2="123.4" stroke="#0a92d8" stroke-width=".6"/>
      <g class="axis" text-anchor="middle">
        <text x="16.5" y="130">Jan</text><text x="30" y="130">Feb</text><text x="43.5" y="130">Mar</text>
        <text x="57" y="130">Apr</text><text x="70.5" y="130">May</text><text x="84" y="130">Jun</text>
        <text x="97.5" y="130">Jul</text><text x="111" y="130">Aug</text><text x="124.5" y="130">Sep</text>
        <text x="138" y="130">Oct</text><text x="151.5" y="130">Nov</text><text x="165" y="130">Dec</text>
      </g>
    </svg>
  </div>

  <div class="card trades">
    <div class="card-label">Opened and Recent Trades</div>
    <div class="pager"><span></span><span></span></div>
    <table class="trade-table">
      <thead>
        <tr><th style="padding-left:25px;width:94px">Ticker Name</th><th style="width:87px">Logo of the Ticker</th><th style="width:64px">Entry Price</th><th style="width:91px">Status (Open/Close)</th><th style="width:58px">Exit Price</th><th style="width:87px">Current Profit in $</th><th>%</th></tr>
      </thead>
      <tbody>
        <tr><td style="padding-left:24px">LOREM</td><td class="logo-cell">LOGO</td><td>$52.45</td><td>OPEN</td><td>$42.45</td><td>$26.867</td><td>60%</td></tr>
        <tr><td style="padding-left:24px">LOREM</td><td class="logo-cell">LOGO</td><td>$52.45</td><td>OPEN</td><td>$42.45</td><td>$26.867</td><td>60%</td></tr>
        <tr><td style="padding-left:24px">LOREM</td><td class="logo-cell">LOGO</td><td>$52.45</td><td>OPEN</td><td>$42.45</td><td>$26.867</td><td>60%</td></tr>
      </tbody>
    </table>
  </div>

  <p class="footer">© 2024 Trading Journal.All Rights Reserved &nbsp;|&nbsp; Privacy &nbsp;|&nbsp; Terms of Use</p>
</section>

</body>
</html>
```